Voucher design for Willow Brook Spa

1) Create a creative design and voucher for Willow Brook Spa that create a lasting memory for the audience. I would like to give out vouchers to all neighbours.
2) Kindly look at the website www.willowbrookspa-example.net
3) Content must include logo, address, telephone number and website.

Here is the content of the voucher

2) 15 dollar cash voucher - off full body massage
3) 10 dollars cash voucher - off foot massage
(Both the fully body massage and foot massage, slimming massage vouchers must be separated and separate vouchers and independent)
4) 20 dollars cash voucher - off slimming massage

Terms and conditions at the back of the voucher
1) Willow Brook Spa reserved the right to amend change the terms and conditions without prior notice.
2) This promotional is not valid with any other promotions existing. e.g
3) Each person is entitled to use one voucher at any one time.

Target Market(s)

Mass market

Font styles to use
Decorative

Requirements
Must have
• 1) Creatives cash vouchers and beautiful design
• 2) Logo fo the company
• 3) Address and telephone number
• 4) website
• 5) Terms and conditions
Nice to have
• You can use tree or lotus as the symbol but it must be toward nature, beautiful, eye catching and creative.

```html
<!DOCTYPE html>
<html lang="en">
<head>
<meta charset="utf-8">
<title>Willow Brook Spa – Voucher Postcard</title>
<link href="https://fonts.googleapis.com/css2?family=Roboto+Condensed:wght@400;500;700&display=swap" rel="stylesheet">
<style>
  :root {
    --spa-blue: #1f5fae;
    --spa-green: #7ab944;
    --text-dark: #2e2e2e;
    --text-soft: #4a4a4a;
    --line-grey: #555555;
    --stamp-grey: #5a5a5a;
    --paper: #ffffff;
  }
  * { margin: 0; padding: 0; box-sizing: border-box; }
  html, body { width: 900px; height: 1200px; overflow: hidden; background: var(--paper); }
  body { font-family: "Roboto Condensed", "Arial Narrow", sans-serif; color: var(--text-dark); }

  .sheet { position: relative; width: 900px; height: 1200px; background: var(--paper); }

  .card {
    position: absolute; left: 102px; width: 678px;
    background: var(--paper);
    box-shadow: 0 0 3px rgba(0,0,0,0.35);
    overflow: hidden;
  }
  .card--front { top: 66px; height: 524px; }
  .card--back  { top: 610px; height: 525px; }
  .card__art { position: absolute; inset: 0; width: 100%; height: 100%; }

  /* Front */
  .brand {
    position: absolute; left: 433px; top: 62px; width: 200px;
    display: flex; flex-direction: column; align-items: center; gap: 10px;
  }
  .brand__dot { width: 44px; height: 44px; border-radius: 50%; background: var(--spa-green); }
  .brand__name {
    font-weight: 700; font-size: 19px; color: var(--spa-blue);
    letter-spacing: 0.5px; white-space: nowrap;
  }
  .headline {
    position: absolute; left: 377px; top: 186px;
    font-weight: 700; font-size: 35px; line-height: 40px; color: var(--spa-blue);
    letter-spacing: 0.2px; white-space: nowrap;
  }
  .subhead {
    position: absolute; left: 378px; top: 228px;
    font-weight: 700; font-size: 21px; line-height: 24px; color: var(--spa-green);
    white-space: nowrap;
  }
  .services {
    position: absolute; left: 382px; top: 274px; width: 270px;
    list-style: none; font-weight: 500; font-size: 16px; line-height: 20px; color: var(--text-dark);
  }
  .services li { position: relative; padding-left: 18px; }
  .services li::before {
    content: ""; position: absolute; left: 1px; top: 6px;
    width: 10px; height: 10px; border-radius: 50%; background: var(--spa-blue);
  }
  .website {
    position: absolute; left: 50px;
    font-weight: 700; font-size: 14px; line-height: 16px; letter-spacing: 2px; color: var(--spa-blue);
    white-space: nowrap;
  }
  .card--front .website { top: 480px; }
  .card--back .website { top: 487px; }
  .contact {
    position: absolute; left: 50px; top: 500px;
    font-weight: 500; font-size: 12px; line-height: 14px; color: var(--text-soft);
    white-space: nowrap;
  }

  /* Back */
  .voucher { position: absolute; }
  .voucher__amount {
    font-weight: 700; font-size: 25px; line-height: 28px; color: var(--spa-blue);
    white-space: nowrap;
  }
  .voucher__detail {
    font-weight: 700; font-size: 11.5px; line-height: 13px; color: #222;
  }
  .voucher--body  { left: 16px;  top: 261px; width: 118px; }
  .voucher--foot  { left: 154px; top: 259px; width: 120px; }
  .voucher--slim  { left: 18px;  top: 331px; width: 124px; }
  .voucher-divider {
    position: absolute; left: 147px; top: 262px; width: 2px; height: 124px;
    background: var(--spa-green);
  }
  .terms {
    position: absolute; left: 440px; top: 414px; width: 215px;
    font-size: 9.5px; line-height: 11.5px; color: var(--text-soft);
  }
  .terms__title {
    font-weight: 700; font-size: 10.5px; color: var(--spa-blue);
    text-transform: uppercase; letter-spacing: 0.5px; margin-bottom: 2px;
  }
  .terms ol { padding-left: 12px; }
</style>
</head>
<body>
<main class="sheet">

  <!-- Front of postcard -->
  <section class="card card--front">
    <svg class="card__art" viewBox="0 0 678 524">
      <defs>
        <linearGradient id="frontPanel" x1="0" y1="0" x2="0" y2="1">
          <stop offset="0" stop-color="#ffffff"/>
          <stop offset="0.55" stop-color="#f3f4f5"/>
          <stop offset="1" stop-color="#dfe3e6"/>
        </linearGradient>
        <linearGradient id="massagePhoto" x1="0" y1="0" x2="1" y2="1">
          <stop offset="0" stop-color="#f1dcc6"/>
          <stop offset="0.5" stop-color="#d99a6c"/>
          <stop offset="1" stop-color="#b8704a"/>
        </linearGradient>
        <linearGradient id="stonesPhoto" x1="0" y1="0" x2="1" y2="1">
          <stop offset="0" stop-color="#5c5f63"/>
          <stop offset="0.6" stop-color="#3a3c3f"/>
          <stop offset="1" stop-color="#b04ea5"/>
        </linearGradient>
        <linearGradient id="leafSpray" x1="0" y1="0" x2="1" y2="1">
          <stop offset="0" stop-color="#dbe9f6"/>
          <stop offset="1" stop-color="#e3f0d8"/>
        </linearGradient>
      </defs>

      <rect width="678" height="524" fill="url(#frontPanel)"/>

      <g role="img" aria-label="Soft scattered blue and green leaves">
        <rect x="572" y="0" width="106" height="104" fill="url(#leafSpray)" opacity="0.8"/>
      </g>

      <g role="img" aria-label="Photo of a smiling man receiving a back massage beside lit candles">
        <path d="M0 0 H450 C380 60 335 150 322 250 C312 330 282 378 200 394 C130 404 60 402 0 396 Z" fill="url(#massagePhoto)"/>
      </g>

      <path d="M0 426 C90 440 200 440 262 410 C300 390 322 360 334 326 C326 382 294 424 232 444 C150 466 60 458 0 450 Z" fill="var(--spa-green)"/>
      <path d="M450 0 H560 C430 70 362 160 345 262 C333 352 292 412 205 424 C120 434 50 430 0 426 V396 C60 402 130 404 200 394 C282 378 312 330 322 250 C335 150 380 60 450 0 Z" fill="var(--spa-blue)"/>

      <g role="img" aria-label="Photo of stacked black spa stones with a pink orchid">
        <rect x="340" y="412" width="200" height="112" rx="40" fill="url(#stonesPhoto)"/>
      </g>

      <path d="M678 362 C592 400 546 460 520 524 H548 C566 488 606 440 678 410 Z" fill="var(--spa-green)"/>
      <path d="M678 410 C606 440 566 488 548 524 H678 Z" fill="var(--spa-blue)"/>
    </svg>

    <div class="brand">
      <span class="brand__dot"></span>
      <span class="brand__name">Willow Brook Spa</span>
    </div>

    <h1 class="headline">COME EXPERIENCE</h1>
    <h2 class="subhead">THE SECRETS OF RELAXATION</h2>
    <ul class="services">
      <li>Full body massage</li>
      <li>Foot massage</li>
      <li>Slimming massage</li>
      <li>One separate voucher for each treatment</li>
    </ul>

    <p class="website">www.willowbrookspa-example.net</p>
    <p class="contact">18 Meadow Lane, Brookfield &nbsp;|&nbsp; Tel (555) 014-2270</p>
  </section>

  <!-- Back of postcard -->
  <section class="card card--back">
    <svg class="card__art" viewBox="0 0 678 525">
      <defs>
        <linearGradient id="lakePhoto" x1="0" y1="0" x2="0" y2="1">
          <stop offset="0" stop-color="#b9cfe0"/>
          <stop offset="0.35" stop-color="#4f7a5a"/>
          <stop offset="0.7" stop-color="#5f8fa6"/>
          <stop offset="1" stop-color="#7b7f7a"/>
        </linearGradient>
        <linearGradient id="relaxPhoto" x1="0" y1="0" x2="1" y2="1">
          <stop offset="0" stop-color="#c8576a"/>
          <stop offset="0.5" stop-color="#e9c2a6"/>
          <stop offset="1" stop-color="#6b4632"/>
        </linearGradient>
        <linearGradient id="voucherPanel" x1="0" y1="0" x2="0" y2="1">
          <stop offset="0" stop-color="#ffffff"/>
          <stop offset="1" stop-color="#eef0f2"/>
        </linearGradient>
      </defs>

      <rect width="678" height="525" fill="var(--paper)"/>
      <path d="M0 180 H340 C310 230 295 300 300 360 C300 400 320 460 400 525 H0 Z" fill="url(#voucherPanel)"/>

      <g role="img" aria-label="Photo of a man meditating on a rock by a calm mountain lake">
        <path d="M0 0 H462 C420 50 382 110 344 168 C250 190 120 196 0 184 Z" fill="url(#lakePhoto)"/>
      </g>
      <path d="M0 184 C120 196 250 190 344 168" fill="none" stroke="var(--spa-blue)" stroke-width="3"/>

      <path d="M0 450 C120 455 222 420 286 300 L300 262 C296 342 330 440 410 525 H0 Z" fill="var(--spa-green)"/>
      <path d="M0 424 C120 430 212 398 276 300 L290 290 C226 418 120 456 0 452 Z" fill="var(--spa-blue)"/>

      <path d="M462 0 H545 C425 80 332 170 312 262 C297 342 332 440 420 525 H400 C300 440 275 340 292 260 C312 170 392 80 462 0 Z" fill="var(--spa-blue)"/>

      <circle cx="243" cy="400" r="66" fill="var(--paper)"/>
      <circle cx="243" cy="400" r="62" fill="var(--spa-blue)"/>
      <circle cx="243" cy="400" r="57" fill="var(--paper)"/>
      <g role="img" aria-label="Photo of a woman relaxing during a hot stone treatment">
        <circle cx="243" cy="400" r="53" fill="url(#relaxPhoto)"/>
      </g>

      <rect x="553" y="90" width="80" height="95" fill="var(--stamp-grey)"/>

      <g stroke="var(--line-grey)" stroke-width="3">
        <line x1="425" y1="308" x2="628" y2="308"/>
        <line x1="425" y1="352" x2="628" y2="352"/>
        <line x1="425" y1="395" x2="628" y2="395"/>
      </g>
    </svg>

    <div class="voucher voucher--body">
      <p class="voucher__amount">15 DOLLAR</p>
      <p class="voucher__detail">cash voucher - off full body massage</p>
    </div>
    <span class="voucher-divider"></span>
    <div class="voucher voucher--foot">
      <p class="voucher__amount">10 DOLLARS</p>
      <p class="voucher__detail">cash voucher off foot massage</p>
    </div>
    <div class="voucher voucher--slim">
      <p class="voucher__amount">20 DOLLARS</p>
      <p class="voucher__detail">cash voucher - off slim-<br>ming massage</p>
    </div>

    <div class="terms">
      <p class="terms__title">Terms &amp; Conditions</p>
      <ol>
        <li>Willow Brook Spa reserves the right to amend the terms and conditions without prior notice.</li>
        <li>Not valid with any other existing promotion.</li>
        <li>One voucher per person at any one time.</li>
      </ol>
    </div>

    <p class="website">www.willowbrookspa-example.net</p>
  </section>

</main>
</body>
</html>
```